Love Your Hearing - Life Sounds Good

I need a website. I had a company doing it, and it looked very nice, but they went way up on hosting costs and said they owned the design of the site. I changed hosts to keep costs down. You can see the current design at crestvaleaudio.com. They said I could use the copy and images from the current website. So you could cut and paste to speed things up. My logo and other images are on the current website. If you are unable to use I can send other digital copies.

Target Market(s)

seniors 55 and up

Number of Pages Required

4 page

Font styles to use
Sans Serif

Colors
0255a3
f78f20

Requirements
Must have
• Video testimonies that I can add without assistance. I use youtube links for the videos.
Nice to have
• The color scheme theme can be drawn from the logo, which is on the current webstie crestvaleaudio.com
Should not have
• Should not have anything related to SonoPath on the website.

```html
<!DOCTYPE html>
<html lang="en">
<head>
<meta charset="utf-8">
<title>Crestvale Hearing Center</title>
<link href="https://fonts.googleapis.com/css2?family=Cinzel:wght@400;600;700&family=Montserrat:ital,wght@0,400;0,500;0,600;1,400&display=swap" rel="stylesheet">
<style>
:root{
  --blue:#0f58a0;
  --blue-deep:#0d4f93;
  --orange:#f78f20;
  --orange-soft:#f59a47;
  --orange-mid:#f5913a;
  --ink:#555;
  --ink-light:#777;
  --grey-bg:#f4f4f4;
  --dark:#2e2e2e;
  --white:#fff;
}
*{margin:0;padding:0;box-sizing:border-box}
html,body{width:1200px;height:3938px;overflow:hidden;background:var(--white)}
body{font-family:"Montserrat",sans-serif;color:var(--ink);position:relative}
.display{font-family:"Cinzel",serif}
section,header{position:absolute;left:0;width:1200px}
.abs{position:absolute}

/* header */
.site-header{top:0;height:124px;background:var(--white)}
.topbar{position:absolute;left:230px;top:0;width:970px;height:41px}
.topbar-info{position:absolute;top:0;height:41px;display:flex;align-items:center;gap:8px;color:var(--white);font-size:13px}
.brand{position:absolute;left:66px;top:18px;width:130px;text-align:center}
.brand-mark{width:48px;height:48px;border-radius:50%;background:var(--orange);margin:0 auto 6px}
.brand-name{font-family:"Cinzel",serif;font-weight:700;font-size:16px;color:var(--blue);line-height:1.05;letter-spacing:.5px}
.main-nav{position:absolute;right:78px;top:73px;display:flex;gap:27px;font-size:13.5px;color:#666;letter-spacing:.3px}
.main-nav .active{color:var(--blue)}

/* hero */
.hero{top:124px;height:543px}
.hero-photo{position:absolute;inset:0;background:linear-gradient(100deg,#3a2a26 0%,#4b3a33 30%,#2d2a2c 60%,#1e1d21 100%)}
.hero-photo::after{content:"";position:absolute;inset:0;background:radial-gradient(ellipse at 35% 40%,rgba(140,70,55,.45),transparent 60%)}
.hero-title{position:absolute;top:195px;width:100%;text-align:center;color:var(--white);font-size:46px;font-weight:600;letter-spacing:1px}
.hero-sub{position:absolute;top:276px;width:100%;text-align:center;color:var(--white);font-size:23px}

/* quick links */
.quick-links{top:667px;height:134px;display:flex}
.quick-link{flex:1;display:flex;align-items:center;justify-content:center;gap:24px;color:var(--white)}
.quick-link:nth-child(1){background:var(--orange-soft)}
.quick-link:nth-child(2){background:var(--orange-mid)}
.quick-link:nth-child(3){background:var(--orange)}
.quick-link .ring{width:68px;height:68px;border:2px solid var(--white);border-radius:50%;display:flex;align-items:center;justify-content:center}
.quick-link .label{font-family:"Cinzel",serif;font-size:21px;line-height:1.45;letter-spacing:.5px}

/* welcome */
.welcome{top:801px;height:625px}
.welcome-accent{left:76px;top:158px;width:126px;height:374px;background:var(--blue)}
.welcome-photo{left:142px;top:99px;width:333px;height:375px;background:linear-gradient(135deg,#e2e2e2,#bdbdbd)}
.welcome-copy{left:570px;top:104px;width:560px}
.welcome-copy h2{font-size:30px;font-weight:400;color:var(--blue);line-height:1.6;letter-spacing:0;white-space:nowrap}
.welcome-copy h2 span{color:var(--orange)}
.welcome-copy p{font-size:13px;line-height:25px;color:var(--ink-light)}
.welcome-copy .lead{margin-top:20px}
.welcome-copy h3{font-size:19px;font-weight:400;color:var(--orange);margin:18px 0 10px}
.btn{display:inline-block;background:var(--blue);color:var(--white);font-family:"Cinzel",serif;font-weight:700;font-size:17px;letter-spacing:.5px;text-align:center;line-height:51px;height:51px;width:208px;border-radius:3px}
.welcome-copy .btn{margin-top:22px;margin-left:3px}

/* services */
.services{top:1426px;height:959px;background:var(--grey-bg)}
.section-title{position:absolute;width:100%;text-align:center;font-size:33px;font-weight:700;color:var(--blue);letter-spacing:.3px}
.section-title span{color:var(--orange)}
.service-card{position:absolute;width:323px;height:312px;background:var(--white);box-shadow:0 2px 6px rgba(0,0,0,.08)}
.service-card .photo{height:229px}
.service-card .foot{height:83px;display:flex;align-items:center;justify-content:space-between;padding:0 19px;font-size:17px;color:#666}
.arrow-ring{width:30px;height:30px;border:2px solid var(--orange);border-radius:50%;display:flex;align-items:center;justify-content:center}

/* testimonials */
.testimonials{top:2385px;height:593px}
.testimonials-bg{position:absolute;inset:0;background:linear-gradient(120deg,#3b3836,#2d2c2c 50%,#262626)}
.testimonials h2{position:absolute;left:78px;top:103px;font-size:33px;font-weight:700;color:var(--white)}
.quote-box{left:76px;top:174px;width:563px;height:291px;background:var(--orange);color:var(--white);padding:60px 28px 0}
.quote-box p{font-style:italic;font-size:19.5px;line-height:31px;margin-top:22px;width:420px}
.quote-box .by{font-size:16px;margin-top:12px}
.video-main{left:602px;top:82px;width:520px;height:312px;background:linear-gradient(135deg,#b9a89c,#8f98a9 55%,#6d7486)}
.thumb{top:419px;width:144px;height:93px}

/* ways */
.ways{top:2978px;height:480px}
.way{position:absolute;top:121px;width:188px;height:185px;border:2px solid #e3e3e3;background:var(--white);text-align:center}
.way svg{margin-top:42px}
.way span{display:block;margin-top:12px;font-size:14px;color:#555}

/* newsletter */
.newsletter{top:3458px;height:480px;background:var(--blue);color:var(--white)}
.newsletter h2{position:absolute;width:100%;top:47px;text-align:center;font-size:34px;font-weight:600;letter-spacing:1.5px}
.newsletter .intro{position:absolute;width:100%;top:100px;text-align:center;font-size:17px}
.signup{left:339px;top:148px;width:520px;height:46px;border:2px solid var(--white);border-radius:23px;display:flex;align-items:center;justify-content:space-between;padding:0 3px 0 22px;font-size:13px}
.signup .go{background:var(--white);color:var(--blue);font-family:"Cinzel",serif;font-weight:700;font-size:16px;height:36px;line-height:36px;padding:0 18px;border-radius:18px;letter-spacing:.5px}
.contact{position:absolute;top:257px;width:360px;text-align:center;font-size:13.5px;line-height:23px}
.contact svg{display:block;margin:0 auto 14px}
.divider{position:absolute;top:285px;width:1px;height:30px;background:rgba(255,255,255,.35)}
.copyright{position:absolute;width:100%;top:440px;text-align:center;font-size:13px}
</style>
</head>
<body>

<header class="site-header">
  <svg class="topbar" viewBox="0 0 970 41" aria-hidden="true"><path d="M0 0H970V41H40C26 41 20 24 0 0Z" fill="var(--blue)"/></svg>
  <div class="topbar-info" style="left:625px">
    <svg width="14" height="18" viewBox="0 0 14 18"><path d="M7 0C3 0 0 3 0 7c0 5 7 11 7 11s7-6 7-11c0-4-3-7-7-7z" fill="var(--orange)"/><circle cx="7" cy="7" r="2.5" fill="var(--blue)"/></svg>
    <span style="margin-left:6px">240 W. Oak St Suite 210 Crestvale, NC 28099</span>
  </div>
  <div class="topbar-info" style="left:990px">
    <svg width="17" height="17" viewBox="0 0 24 24"><path d="M6.6 10.8a15 15 0 006.6 6.6l2.2-2.2c.3-.3.7-.4 1-.2 1.1.4 2.3.6 3.6.6.6 0 1 .4 1 1V20c0 .6-.4 1-1 1A17 17 0 013 4c0-.6.4-1 1-1h3.5c.6 0 1 .4 1 1 0 1.3.2 2.5.6 3.6.1.3 0 .7-.2 1z" fill="var(--orange)"/></svg>
    <span style="margin-left:6px">(555) 014-2290</span>
  </div>
  <div class="brand">
    <div class="brand-mark"></div>
    <div class="brand-name">CRESTVALE</div>
  </div>
  <nav class="main-nav">
    <span class="active">HOME</span><span>HEARING AIDS</span><span>SERVICES</span><span>EDUCATION</span><span>ABOUT US</span><span>NEWS</span><span>CONTACT</span>
  </nav>
</header>

<section class="hero">
  <div class="hero-photo" role="img" aria-label="Couple beside a canoe on a misty lakeshore at dusk"></div>
  <h1 class="hero-title display">RECAPTURE THE SOUND OF LIFE</h1>
  <p class="hero-sub">and the intimacy of a quiet conversation</p>
</section>

<section class="quick-links">
  <div class="quick-link">
    <div class="ring"><svg width="26" height="30" viewBox="0 0 26 30"><path d="M13 1a10 10 0 00-6 18v4h12v-4A10 10 0 0013 1z" fill="var(--white)"/><rect x="8" y="25" width="10" height="3" rx="1" fill="var(--white)"/><path d="M13 8v9M10 13l3 4 3-4" stroke="var(--orange-soft)" stroke-width="2" fill="none"/></svg></div>
    <div class="label">TIPS FOR<br>WEARERS</div>
  </div>
  <div class="quick-link">
    <div class="ring"><svg width="30" height="30" viewBox="0 0 30 30"><path d="M15 2a13 13 0 00-11 20l-2 6 6-2A13 13 0 1015 2z" fill="var(--white)"/><text x="15" y="21" text-anchor="middle" font-family="Montserrat,sans-serif" font-weight="700" font-size="17" fill="var(--orange-mid)">?</text></svg></div>
    <div class="label">FAQ</div>
  </div>
  <div class="quick-link">
    <div class="ring"><svg width="28" height="28" viewBox="0 0 28 28"><rect x="2" y="5" width="24" height="21" rx="3" fill="var(--white)"/><rect x="7" y="1" width="3" height="7" rx="1" fill="var(--white)"/><rect x="18" y="1" width="3" height="7" rx="1" fill="var(--white)"/><rect x="2" y="11" width="24" height="2" fill="var(--orange)"/></svg></div>
    <div class="label">SCHEDULE<br>APPOINMENT</div>
  </div>
</section>

<section class="welcome">
  <div class="abs welcome-accent"></div>
  <div class="abs welcome-photo" role="img" aria-label="Portrait of the hearing specialist in a white coat"></div>
  <div class="abs welcome-copy">
    <h2 class="display">WELCOME TO<br>CRESTVALE <span>HEARING CENTER LLC</span></h2>
    <p class="lead">We provide hearing evaluations, counseling, and fitting of hearing aids. We service all the major brands of hearing aids including Tovarin, Quellix, Brisdane, Harvolo, Myrlund, Pellatide, Zorvane, Ostrevin, Calyndra, Vintrello, Dessamoor, and others.</p>
    <h3>Meet the Specialist, Edward Hollis</h3>
    <p>"I was first introduced to hearing aids as a patient. At the tender age of 36, I was diagnosed with profound hearing loss by a hearing healthcare provider in Raleigh.</p>
    <span class="btn">KNOW MORE</span>
  </div>
</section>

<section class="services">
  <h2 class="section-title display" style="top:52px">SERVICES <span>WE PROVIDE</span></h2>

  <div class="service-card" style="left:76px;top:119px"><div class="photo" role="img" aria-label="Otoscope held to a patient's ear" style="background:linear-gradient(135deg,#dcdcdc,#8d8d8d)"></div><div class="foot">Hearing Evaluations<span class="arrow-ring"><svg width="14" height="12" viewBox="0 0 14 12"><path d="M1 6h11M7 1l5 5-5 5" stroke="var(--orange)" stroke-width="2" fill="none"/></svg></span></div></div>
  <div class="service-card" style="left:438px;top:119px"><div class="photo" role="img" aria-label="Specialist examining a patient's ear with a video screen behind" style="background:linear-gradient(135deg,#c9ced6,#e4e6e9 50%,#2b3142)"></div><div class="foot">Video Otoscopy<span class="arrow-ring"><svg width="14" height="12" viewBox="0 0 14 12"><path d="M1 6h11M7 1l5 5-5 5" stroke="var(--orange)" stroke-width="2" fill="none"/></svg></span></div></div>
  <div class="service-card" style="left:800px;top:119px"><div class="photo" role="img" aria-label="Hands fitting a hearing aid behind an ear" style="background:linear-gradient(135deg,#2f6a6a,#8c9b9a 55%,#d7c2b3)"></div><div class="foot">Hearing Aid Fitting<span class="arrow-ring"><svg width="14" height="12" viewBox="0 0 14 12"><path d="M1 6h11M7 1l5 5-5 5" stroke="var(--orange)" stroke-width="2" fill="none"/></svg></span></div></div>

  <div class="service-card" style="left:76px;top:474px"><div class="photo" role="img" aria-label="Doctor checking an older man's ear with an otoscope" style="background:linear-gradient(135deg,#9c7a5c,#e7e2dc 60%,#cfcfcf)"></div><div class="foot">Follow Up Service<span class="arrow-ring"><svg width="14" height="12" viewBox="0 0 14 12"><path d="M1 6h11M7 1l5 5-5 5" stroke="var(--orange)" stroke-width="2" fill="none"/></svg></span></div></div>
  <div class="service-card" style="left:438px;top:474px"><div class="photo" role="img" aria-label="Ear highlighted in red showing discomfort" style="background:radial-gradient(circle at 55% 50%,#d2403a,#8b5a50 55%,#4a4a4a)"></div><div class="foot">Ear Molds<span class="arrow-ring"><svg width="14" height="12" viewBox="0 0 14 12"><path d="M1 6h11M7 1l5 5-5 5" stroke="var(--orange)" stroke-width="2" fill="none"/></svg></span></div></div>
  <div class="service-card" style="left:800px;top:474px"><div class="photo" role="img" aria-label="A row of modern hearing aid devices" style="background:linear-gradient(180deg,#ececec,#dedede)"></div><div class="foot">Wireless Technology<span class="arrow-ring"><svg width="14" height="12" viewBox="0 0 14 12"><path d="M1 6h11M7 1l5 5-5 5" stroke="var(--orange)" stroke-width="2" fill="none"/></svg></span></div></div>

  <span class="btn abs" style="left:496px;top:829px">EXPLORE MORE</span>
</section>

<section class="testimonials">
  <div class="testimonials-bg" role="img" aria-label="Dimmed photo of a patient in a consultation"></div>
  <h2 class="display">VIDEO TESTIMONIALS</h2>
  <div class="abs quote-box">
    <svg width="56" height="38" viewBox="0 0 56 38"><path d="M2 38V20C2 8 8 2 22 0v8c-7 2-9 5-9 10h9v20zM34 38V20C34 8 40 2 54 0v8c-7 2-9 5-9 10h9v20z" fill="var(--white)"/></svg>
    <p>“If you need hearing aids or have a hearing problem, come see Eddie Hollis.”</p>
    <div class="by">- Tom Ashworth</div>
  </div>
  <div class="abs video-main" role="img" aria-label="Video testimonial: two men seated in the clinic office"></div>
  <div class="abs thumb" style="left:663px;background:linear-gradient(135deg,#d9d2c8,#5b5a60)" role="img" aria-label="Video thumbnail: a woman's testimonial"></div>
  <div class="abs thumb" style="left:819px;background:linear-gradient(135deg,#e8e2dc,#6a3fa0)" role="img" aria-label="Video thumbnail: a man in a purple shirt"></div>
  <div class="abs thumb" style="left:976px;background:linear-gradient(135deg,#c9b4a3,#7b8ca8)" role="img" aria-label="Video thumbnail: two men seated"></div>
</section>

<section class="ways">
  <h2 class="section-title display" style="top:48px">50 WAYS TO LOVE <span>YOUR HEARING</span></h2>
  <div class="way" style="left:76px">
    <svg width="64" height="56" viewBox="0 0 64 56" fill="none" stroke="var(--orange)" stroke-width="2.5"><path d="M4 12h30v22H18l-9 8v-8H4z"/><path d="M40 6h20v22h-6v7l-7-7h-7z"/></svg>
    <span>Quiet Conversation</span>
  </div>
  <div class="way" style="left:291px">
    <svg width="64" height="56" viewBox="0 0 64 56" fill="none" stroke="var(--orange)" stroke-width="2.5"><path d="M8 40c14 4 34 0 48-10"/><path d="M22 34l4 14M38 32l2 12"/><circle cx="46" cy="14" r="6"/></svg>
    <span>Bird Song</span>
  </div>
  <div class="way" style="left:506px">
    <svg width="64" height="56" viewBox="0 0 64 56" fill="none" stroke="var(--orange)" stroke-width="2.5"><path d="M24 44c0 6 10 6 12 0 2-6 10-10 10-20a14 14 0 00-28 0"/><path d="M10 14a22 22 0 000 24M54 14a22 22 0 010 24"/></svg>
    <span>Hearing Enhancement</span>
  </div>
  <div class="way" style="left:721px">
    <svg width="64" height="56" viewBox="0 0 64 56" fill="none" stroke="var(--orange)" stroke-width="2.5"><path d="M24 44V12l22-6v32"/><ellipse cx="18" cy="44" rx="6" ry="5"/><ellipse cx="40" cy="38" rx="6" ry="5"/></svg>
    <span>Music</span>
  </div>
  <div class="way" style="left:936px">
    <svg width="64" height="56" viewBox="0 0 64 56" fill="none" stroke="var(--orange)" stroke-width="2.5"><rect x="12" y="4" width="40" height="48" rx="14"/><path d="M22 22h20M22 32h20"/></svg>
    <span>Children Laughing</span>
  </div>
  <span class="btn abs" style="left:496px;top:347px">EXPLORE MORE</span>
</section>

<section class="newsletter">
  <h2 class="display">SUBSCRIBE TO OUR NEWSLETTER</h2>
  <p class="intro">Subscribe to our newsletter to get latest info and special offers from us</p>
  <div class="abs signup"><span>Enter your email</span><span class="go">SUBSCRIBE</span></div>

  <div class="contact" style="left:59px">
    <svg width="38" height="38" viewBox="0 0 24 24" fill="none" stroke="var(--white)" stroke-width="1.2"><path d="M6.6 10.8a15 15 0 006.6 6.6l2.2-2.2c.3-.3.7-.4 1-.2 1.1.4 2.3.6 3.6.6.6 0 1 .4 1 1V20c0 .6-.4 1-1 1A17 17 0 013 4c0-.6.4-1 1-1h3.5c.6 0 1 .4 1 1 0 1.3.2 2.5.6 3.6.1.3 0 .7-.2 1z"/></svg>
    (555) 014-2290
  </div>
  <div class="divider" style="left:420px"></div>
  <div class="contact" style="left:420px">
    <svg width="32" height="40" viewBox="0 0 32 40" fill="none" stroke="var(--white)" stroke-width="1.8"><path d="M16 2C8 2 2 8 2 15c0 10 14 23 14 23s14-13 14-23C30 8 24 2 16 2z"/><circle cx="16" cy="15" r="5"/></svg>
    240 W. Oak St Suite 210 Crestvale,<br>NC 28099
  </div>
  <div class="divider" style="left:780px"></div>
  <div class="contact" style="left:781px">
    <svg width="38" height="38" viewBox="0 0 38 38" fill="none" stroke="var(--white)" stroke-width="1.8"><path d="M3 16v19h32V16"/><path d="M3 16l16 11 16-11"/><path d="M9 20V3h20v17"/><path d="M13 9h12M13 14h12"/></svg>
    info@crestvaleaudio.com
  </div>

  <p class="copyright">2019 ©CRESTVALE HEARING CENTER - All Rights Reserved.</p>
</section>

</body>
</html>
```